Poster Design Project

Poster with modern feeling to be displayed in office. The text that needs to be included in this poster is below:

Rules
1. If it’s not in writing it doesn’t exist.
2. No such thing as 'off the record.'
3. Do not hold a private conversation in a public place.
4. Don’t believe any number that ends in zero.
5. Never turn down an opportunity to eat or go to the bathroom.
6. Don’t spend any of your own money. Don’t even admit you own a credit card. Don’t spend money that is not yours.
7. Not always a 'right' or 'wrong' answer - 'It depends.'
8. In a campaign, someone has to be in charge – campaigns are a place to foster democracy, not practice it.
9. Assume nothing.
10. If you make a mistake, fix it before analyzing. Bad news doesn’t age well.

Industry/Entity Type

Credit Card

Requirements
Must have
• Rules
7. Not always a “right” or “wrong” answer - 'It depends.' 
9. Assume nothing.

```html
<!DOCTYPE html>
<html lang="en">
<head>
<meta charset="utf-8">
<title>Rules</title>
<link rel="stylesheet" href="https://fonts.googleapis.com/css2?family=Gochi+Hand&family=Patrick+Hand&display=swap">
<style>
  :root {
    --kraft: #cba77c;
    --kraft-dark: #bf9a6e;
    --ink: #2f2b28;
    --ink-blue: #3a3d9c;
    --white: #ffffff;
    --teal: #3f9b8f;
    --orange: #e38a4c;
    --mustard: #d9b23c;
    --taupe: #9c8372;
    --rose: #d9505f;
    --olive: #a4a23c;
    --marker: #fff200;
  }
  * { box-sizing: border-box; margin: 0; padding: 0; }
  html, body { width: 982px; height: 1200px; overflow: hidden; }
  body {
    position: relative;
    background: radial-gradient(ellipse at 50% 40%, var(--kraft) 0%, var(--kraft-dark) 100%);
    font-family: "Patrick Hand", "Comic Sans MS", cursive;
    color: var(--ink);
  }
  .poster-title {
    position: absolute; left: 0; right: 0; top: 30px;
    text-align: center;
    font-family: "Gochi Hand", "Patrick Hand", cursive;
    font-size: 104px; font-weight: 400; letter-spacing: 2px;
    color: var(--ink);
  }
  .rule { position: absolute; }
  .rule-note {
    position: absolute; inset: 0;
    clip-path: polygon(0% 6%, 4% 0%, 12% 5%, 22% 1%, 33% 4%, 45% 0%, 57% 5%, 68% 1%, 80% 4%, 91% 0%, 100% 5%,
      98% 25%, 100% 48%, 97% 72%, 100% 95%, 90% 100%, 78% 96%, 66% 100%, 54% 95%, 42% 100%, 30% 96%, 18% 100%,
      7% 96%, 0% 100%, 2% 75%, 0% 52%, 3% 30%);
  }
  .rule-text {
    position: relative;
    font-size: 34px; line-height: 1.18; letter-spacing: 2.5px;
    white-space: nowrap;
  }
  .marker {
    position: absolute; width: 52px; height: 50px;
    background: var(--marker);
    font-family: "Patrick Hand", cursive; font-size: 30px; color: var(--ink);
  }
  .marker span { position: absolute; }
  .point-right { clip-path: polygon(0 0, 100% 50%, 0 100%); }
  .point-left { clip-path: polygon(100% 0, 0 50%, 100% 100%); }
  .point-down { clip-path: polygon(0 0, 100% 0, 50% 100%); }

  .on-teal { background: var(--teal); }
  .on-orange { background: var(--orange); }
  .on-mustard { background: var(--mustard); }
  .on-taupe { background: var(--taupe); }
  .on-rose { background: var(--rose); }
  .on-olive { background: var(--olive); }
  .text-blue { color: var(--ink-blue); }
  .text-white { color: var(--white); }
</style>
</head>
<body>
  <h1 class="poster-title">Rules</h1>

  <div class="rule" style="left:62px;top:185px;width:385px;height:100px;">
    <div class="rule-note on-teal"></div>
    <p class="rule-text text-blue" style="padding:14px 0 0 28px;">If it's not in WRITING<br>it doesn't exist.</p>
  </div>
  <div class="marker point-right" style="left:55px;top:152px;"><span style="left:6px;top:4px;">1</span></div>

  <div class="rule" style="left:565px;top:195px;width:305px;height:95px;">
    <div class="rule-note on-orange"></div>
    <p class="rule-text text-blue" style="padding:8px 0 0 24px;">No such thing as<br>'off the record.'</p>
  </div>
  <div class="marker point-right" style="left:545px;top:180px;"><span style="left:8px;top:4px;">2</span></div>

  <div class="rule" style="left:125px;top:333px;width:522px;height:97px;">
    <div class="rule-note on-mustard"></div>
    <p class="rule-text" style="padding:8px 0 0 22px;"><b>DO NOT</b> hold a private<br>conversation in a public place.</p>
  </div>
  <div class="marker point-left" style="left:85px;top:328px;"><span style="left:28px;top:4px;">3</span></div>

  <div class="rule" style="left:665px;top:345px;width:242px;height:175px;">
    <div class="rule-note on-taupe"></div>
    <p class="rule-text" style="padding:18px 0 0 24px;">Don't believe<br>any number<br>that ends in<br><b>ZERO.</b></p>
  </div>
  <div class="marker point-left" style="left:628px;top:350px;"><span style="left:28px;top:4px;">4</span></div>

  <div class="rule" style="left:45px;top:432px;width:588px;height:98px;">
    <div class="rule-note on-rose"></div>
    <p class="rule-text text-white" style="padding:18px 0 0 26px;">Never turn down an opportunity<br>to <b>EAT</b> or go to the bathroom.</p>
  </div>
  <div class="marker point-right" style="left:40px;top:415px;"><span style="left:6px;top:4px;">5</span></div>

  <div class="rule" style="left:320px;top:580px;width:626px;height:135px;">
    <div class="rule-note on-olive"></div>
    <p class="rule-text" style="padding:8px 0 0 16px;"><b>DON'T SPEND</b> any of your own money.<br>Don't even admit you own a credit card.<br>Don't spend money that is not yours.</p>
  </div>
  <div class="marker point-left" style="left:276px;top:578px;"><span style="left:28px;top:4px;">6</span></div>

  <div class="rule" style="left:40px;top:640px;width:270px;height:180px;">
    <div class="rule-note on-orange"></div>
    <p class="rule-text" style="padding:12px 0 0 14px;text-indent:42px;">Not always a<br>right or wrong<br>answer –<br>'IT DEPENDS.'</p>
  </div>
  <div class="marker point-right" style="left:40px;top:648px;"><span style="left:6px;top:4px;">7</span></div>

  <div class="rule" style="left:345px;top:790px;width:595px;height:155px;">
    <div class="rule-note on-taupe"></div>
    <p class="rule-text" style="padding:18px 0 0 10px;text-indent:30px;">In a campaign, someone has to be<br>in charge – campaigns are a place to<br>foster democracy, not practice it.</p>
  </div>
  <div class="marker point-left" style="left:320px;top:792px;"><span style="left:28px;top:4px;">8</span></div>

  <div class="rule" style="left:65px;top:870px;width:222px;height:95px;">
    <div class="rule-note on-mustard"></div>
    <p class="rule-text" style="padding:10px 0 0 40px;">Assume<br><b>NOTHING.</b></p>
  </div>
  <div class="marker point-right" style="left:60px;top:855px;"><span style="left:6px;top:4px;">9</span></div>

  <div class="rule" style="left:95px;top:1000px;width:625px;height:110px;">
    <div class="rule-note on-rose"></div>
    <p class="rule-text text-white" style="padding:16px 0 0 22px;">If you make a mistake, <b>FIX IT</b> before<br>analyzing. Bad news doesn't age well.</p>
  </div>
  <div class="marker point-down" style="left:58px;top:985px;width:72px;height:55px;"><span style="left:10px;top:2px;">10</span></div>
</body>
</html>
```